Conceptual Model Diagram for Replacing Medication with Behavior to Support Weight Loss Maintenance

Design a figure of a conceptual model that needs to be inserted into a word document for a PSF grant. This conceptual model illustrates how behavioral strategies can replace the regulatory functions lost after AOM discontinuation. The intervention targets three core vulnerabilities—appetite resurgence, metabolic inflexibility, and suboptimal mindstate—through the domains of Food, Physical Activity, and Mind. Sustained weight loss maintenance occurs at the intersection of these domains. The intervention is delivered within a design framework that makes behaviors easier to perform, aligns them with identity, and reinforces them through virtual support and community, ensuring real-world feasibility and long-term adherence.
Target Market(s)
PSF reviewers
Industry/Entity Type
academic
Other font styles liked:
- arial
Requirements
Must have
- see my attached description

```html
<!DOCTYPE html>
<html lang="en">
<head>
<meta charset="utf-8">
<title>Conceptual Model: Replacing Medication with Behavior for Weight Loss Maintenance</title>
<link rel="stylesheet" href="https://fonts.googleapis.com/css2?family=Arimo:wght@400;700&display=swap">
<style>
  :root {
    --ring-outer: #00b5b9;
    --ring-middle: #53c4c6;
    --ring-inner: #9fd8df;
    --lobe-teal: #12bab4;
    --domain-blue: #216a93;
    --overlap-blue: #1f4870;
    --core-blue: #2a3c69;
    --ink: #111111;
    --paper: #ffffff;
  }
  html, body {
    margin: 0;
    padding: 0;
    width: 957px;
    height: 1200px;
    overflow: hidden;
    background: var(--paper);
  }
  .model-figure {
    display: block;
    width: 957px;
    height: 1200px;
    font-family: "Arimo", Arial, sans-serif;
  }
  .ring--outer { fill: var(--ring-outer); }
  .ring--middle { fill: var(--ring-middle); }
  .ring--inner { fill: var(--ring-inner); }
  .ring--core { fill: var(--paper); }
  .lobe { fill: var(--lobe-teal); }
  .lobe-divider { stroke: var(--paper); stroke-width: 5; }
  .domain { fill: var(--domain-blue); }
  .domain-overlap { fill: var(--overlap-blue); }
  .domain-core { fill: var(--core-blue); }
  .layer-title { font-size: 52px; font-weight: 700; fill: var(--ink); }
  .layer-detail { font-size: 40px; font-weight: 400; fill: var(--ink); }
  .vulnerability { font-size: 44px; font-weight: 700; fill: var(--paper); }
  .domain-label { font-size: 52px; font-weight: 400; fill: var(--paper); text-anchor: middle; }
  .outcome-label { font-size: 46px; font-weight: 700; fill: var(--paper); text-anchor: middle; }
  .caption { font-size: 31px; font-weight: 400; fill: var(--ink); }
</style>
</head>
<body>
<svg class="model-figure" viewBox="0 0 1728 2167" xmlns="http://www.w3.org/2000/svg" role="img" aria-label="Conceptual model: three domains, Mind, Food and Physical Activity, intersect at sustained weight loss maintenance, surrounded by three design layers">
  <defs>
    <path id="arc-top-easy" d="M384 888 A478 478 0 0 1 1340 888"/>
    <path id="arc-top-identity" d="M292 888 A570 570 0 0 1 1432 888"/>
    <path id="arc-top-support" d="M189 888 A673 673 0 0 1 1535 888"/>
    <path id="arc-bottom-easy" d="M325 888 A537 537 0 0 0 1399 888"/>
    <path id="arc-bottom-identity" d="M225 888 A637 637 0 0 0 1499 888"/>
    <path id="arc-bottom-support" d="M120 888 A742 742 0 0 0 1604 888"/>
    <!-- lobe label arcs -->
    <path id="arc-mindstate" d="M535.5 972.7 A250 250 0 0 1 770.4 565.8"/>
    <path id="arc-appetite" d="M915.6 566.4 A250 250 0 0 1 1226 897.5"/>
    <path id="arc-metabolic" d="M615.8 1133.6 A262 262 0 0 0 1108.2 1133.6"/>
    <clipPath id="clip-mind"><circle cx="727" cy="812" r="200"/></clipPath>
    <clipPath id="clip-food"><circle cx="997" cy="812" r="200"/></clipPath>
    <clipPath id="clip-activity"><circle cx="862" cy="1045" r="200"/></clipPath>
  </defs>

  <g class="design-layers">
    <circle class="ring ring--outer" cx="862" cy="888" r="773"/>
    <circle class="ring ring--middle" cx="862" cy="888" r="666"/>
    <circle class="ring ring--inner" cx="862" cy="888" r="561"/>
    <circle class="ring ring--core" cx="862" cy="888" r="457"/>

    <text class="layer-title"><textPath href="#arc-top-support" startOffset="50%" text-anchor="middle">3. Virtual Support and Social Connection</textPath></text>
    <text class="layer-title"><textPath href="#arc-top-identity" startOffset="50%" text-anchor="middle">2. Align with Identity</textPath></text>
    <text class="layer-title"><textPath href="#arc-top-easy" startOffset="50%" text-anchor="middle">1. Make it Easy</textPath></text>

    <text class="layer-detail"><textPath href="#arc-bottom-easy" startOffset="50%" text-anchor="middle">(Habits, Routines, Environment, Low Friction)</textPath></text>
    <text class="layer-detail"><textPath href="#arc-bottom-identity" startOffset="50%" text-anchor="middle">(Self-Concept, Maintain IT Model, Internalization)</textPath></text>
    <text class="layer-detail"><textPath href="#arc-bottom-support" startOffset="50%" text-anchor="middle">(Accessibility, Community, Shared Accountability)</textPath></text>
  </g>

  <g class="vulnerabilities">
    <circle class="lobe" cx="727" cy="812" r="300"/>
    <circle class="lobe" cx="997" cy="812" r="300"/>
    <circle class="lobe" cx="862" cy="1045" r="300"/>
    <line class="lobe-divider" x1="862" y1="540" x2="862" y2="670"/>
    <line class="lobe-divider" x1="670" y1="998" x2="562" y2="1061"/>
    <line class="lobe-divider" x1="1054" y1="998" x2="1162" y2="1061"/>
  </g>

  <g class="domains">
    <circle class="domain" cx="727" cy="812" r="200"/>
    <circle class="domain" cx="997" cy="812" r="200"/>
    <circle class="domain" cx="862" cy="1045" r="200"/>
    <circle class="domain-overlap" cx="997" cy="812" r="200" clip-path="url(#clip-mind)"/>
    <circle class="domain-overlap" cx="862" cy="1045" r="200" clip-path="url(#clip-mind)"/>
    <circle class="domain-overlap" cx="862" cy="1045" r="200" clip-path="url(#clip-food)"/>
    <g clip-path="url(#clip-mind)">
      <circle class="domain-core" cx="997" cy="812" r="200" clip-path="url(#clip-activity)"/>
    </g>
    <polygon class="lobe" points="560,655 594,736 515,746"/>
    <polygon class="lobe" points="1164,655 1130,736 1209,746"/>
    <polygon class="lobe" points="862,1196 822,1250 902,1250"/>
  </g>

  <g class="vulnerability-labels">
    <text class="vulnerability"><textPath href="#arc-mindstate" startOffset="50%" text-anchor="middle">Suboptimal Mindstate</textPath></text>
    <text class="vulnerability"><textPath href="#arc-appetite" startOffset="50%" text-anchor="middle">Appetite Resurgence</textPath></text>
    <text class="vulnerability"><textPath href="#arc-metabolic" startOffset="50%" text-anchor="middle">Metabolic Inflexibility</textPath></text>
  </g>

  <g class="domain-labels">
    <text class="domain-label" x="685" y="810">Mind</text>
    <text class="domain-label" x="1040" y="810">Food</text>
    <text class="domain-label" x="862" y="1080">Physical</text>
    <text class="domain-label" x="862" y="1132">Activity</text>
  </g>

  <g class="outcome">
    <text class="outcome-label" x="862" y="861">Sustained</text>
    <text class="outcome-label" x="862" y="908">Weight Loss</text>
    <text class="outcome-label" x="862" y="955">Maintenance</text>
  </g>

  <g class="caption">
    <text x="90" y="1788">This conceptual model illustrates how behavioral strategies can replace the regulatory functions lost</text>
    <text x="90" y="1830">after AOM discontinuation. The intervention targets three core vulnerabilities—appetite resurgence,</text>
    <text x="90" y="1872">metabolic inflexibility, and suboptimal mindstate—through the domains of Food, Physical Activity,</text>
    <text x="90" y="1913">and Mind. Sustained weight loss maintenance occurs at the intersection of these domains. The</text>
    <text x="90" y="1955">intervention is delivered within a design framework that makes behaviors easier to perform, aligns</text>
    <text x="90" y="1997">them with identity, and reinforces them through virtual support and community, ensuring real-world</text>
    <text x="90" y="2038">feasibility and long-term adherence.</text>
  </g>
</svg>
</body>
</html>
```